Webdesign für Projektmanagement
Zielgruppe
Projektmanagement und Projektsteuerung von Bauvorhaben für Projektentwickler und Bauträger.
Wesentliche Bereiche sind Wirtschaftliche Steuerung, Steuerung der Baustelle und Bauabläufe sowie Steuerung der Marketing und Vertriebsaktivitäten.
Aufgabenstellung
Orientierung am Logo. Logo und Visitenkarte liegen bei. Schriftart Prelo und Prelo Slab.

```html
<!DOCTYPE html>
<html lang="de">
<head>
<meta charset="utf-8">
<title>Veldhaus – Projektmanagement</title>
<link rel="stylesheet" href="https://fonts.googleapis.com/css2?family=Raleway:ital,wght@0,400;0,500;0,600;0,700;1,400&display=swap">
<style>
  :root {
    --navy: #0e2742;
    --page-bg: #03243f;
    --gold: #a38f4c;
    --gold-light: #c4ad69;
    --hero-top: #bca663;
    --hero-bottom: #a89150;
    --bar: rgba(255,255,255,0.12);
    --footer: rgba(80,65,25,0.25);
    --card: #f1f1ef;
    --text: #2c2c2c;
    --muted: #5a5a5a;
    --line: #ececec;
    --white: #ffffff;
  }
  * { box-sizing: border-box; margin: 0; padding: 0; }
  html, body { width: 1036px; height: 1200px; overflow: hidden; }
  body {
    background: var(--page-bg);
    font-family: "Raleway", Arial, sans-serif;
    position: relative;
  }
  .site {
    position: absolute;
    left: 18px; top: 312px;
    width: 1000px; height: 576px;
    display: flex;
    box-shadow: 0 10px 30px rgba(0,0,0,0.35);
  }
  /* Sidebar */
  .sidebar {
    width: 153px; height: 100%;
    background: var(--white);
    position: relative;
  }
  .brand {
    position: absolute; left: 23px; top: 52px;
    font-size: 23px; font-weight: 700; color: var(--navy);
    letter-spacing: -0.2px;
  }
  .nav { position: absolute; top: 141px; left: 0; width: 100%; list-style: none; border-top: 1px solid var(--line); }
  .nav li {
    height: 30.6px; line-height: 30px;
    padding-left: 23px; padding-right: 16px;
    border-bottom: 1px solid var(--line);
    font-size: 8.6px; font-weight: 500; color: var(--navy);
    letter-spacing: 0.3px;
    display: flex; justify-content: space-between; align-items: center;
  }
  .nav li.active { color: var(--gold); font-weight: 600; }
  .nav .chevron { color: var(--gold); font-size: 9px; }
  .nav li.search { color: #9a9a9a; font-style: italic; font-weight: 400; justify-content: flex-start; gap: 6px; }
  .social {
    position: absolute; bottom: 20px; left: 0; width: 100%;
    display: flex; justify-content: center; gap: 11px;
  }
  .social span { width: 8px; height: 8px; border-radius: 50%; background: var(--navy); }

  /* Main */
  .main { flex: 1; position: relative; overflow: hidden; }
  .hero-bg {
    position: absolute; inset: 0;
    background: linear-gradient(160deg, var(--hero-top) 0%, #b49d5a 55%, var(--hero-bottom) 100%);
  }
  .contact-bar {
    position: absolute; top: 0; left: 0; right: 0; height: 29px;
    background: var(--bar);
    display: flex; align-items: center; gap: 17px;
    padding-left: 53px;
    font-size: 8.6px; color: var(--white);
  }
  .contact-bar .item { display: flex; align-items: center; gap: 5px; }
  .contact-bar svg { width: 9px; height: 9px; }
  .eyebrow {
    position: absolute; left: 53px; top: 180px;
    font-size: 15.5px; font-weight: 700; color: var(--navy);
    letter-spacing: 0.3px;
  }
  .headline {
    position: absolute; left: 52px; top: 201px;
    font-size: 46px; font-weight: 400; color: var(--white);
    line-height: 56px; letter-spacing: 1px;
  }
  .cards {
    position: absolute; left: 53px; top: 359px;
    display: flex; gap: 9px;
  }
  .card {
    width: 235px; height: 141px;
    background: var(--card);
    position: relative;
    padding: 9px 12px;
  }
  .card .kicker { font-size: 8.4px; font-style: italic; color: var(--muted); }
  .card .title { margin-top: 8px; font-size: 9.6px; font-weight: 500; color: var(--gold); line-height: 13px; }
  .card .body { margin-top: 7px; font-size: 8.4px; color: var(--text); line-height: 13px; }
  .card .more {
    position: absolute; right: 0; bottom: 0;
    background: var(--navy); color: var(--white);
    font-size: 7.6px; font-weight: 600; letter-spacing: 0.3px;
    padding: 6px 12px;
  }
  .footer {
    position: absolute; left: 0; right: 0; bottom: 0; height: 35px;
    background: var(--footer);
    padding-left: 53px;
    display: flex; align-items: center;
    font-size: 8.6px; color: #5b4e28;
  }
</style>
</head>
<body>
  <div class="site">
    <aside class="sidebar">
      <div class="brand">Veldhaus</div>
      <ul class="nav">
        <li class="active">HOME</li>
        <li>LEISTUNGEN</li>
        <li>ÜBER UNS <span class="chevron">›</span></li>
        <li>PROJEKTE <span class="chevron">›</span></li>
        <li>PARTNER</li>
        <li>KONTAKT</li>
        <li class="search">
          <svg width="7" height="7" viewBox="0 0 10 10"><circle cx="4" cy="4" r="3" fill="none" stroke="#a38f4c" stroke-width="1.6"/><line x1="6.3" y1="6.3" x2="9.3" y2="9.3" stroke="#a38f4c" stroke-width="1.6"/></svg>
          Suchen
        </li>
      </ul>
      <div class="social" aria-label="Soziale Netzwerke">
        <span></span><span></span><span></span><span></span>
      </div>
    </aside>

    <main class="main">
      <div class="hero-bg" role="img" aria-label="Foto: Baupläne mit Brille, Wasserwaage und Papierrollen in goldenem Farbton"></div>

      <div class="contact-bar">
        <span class="item">
          <svg viewBox="0 0 10 10"><path d="M2 0.5 L3.6 2.8 L2.8 3.8 Q4 6.2 6.2 7.2 L7.2 6.4 L9.5 8 L8.2 9.5 Q3 9 0.5 2 Z" fill="#0e2742"/></svg>
          +49 (0)211 - 555 123 40
        </span>
        <span class="item">
          <svg viewBox="0 0 10 10"><circle cx="5" cy="5" r="4.2" fill="none" stroke="#0e2742" stroke-width="1.1"/><path d="M5 2.5 V5 H7" fill="none" stroke="#0e2742" stroke-width="1.1"/></svg>
          Mo - Fr 9:00 - 18:00
        </span>
        <span class="item">
          <svg viewBox="0 0 10 10"><rect x="0.5" y="2" width="9" height="6.5" fill="none" stroke="#0e2742" stroke-width="1.1"/><path d="M0.5 2 L5 5.8 L9.5 2" fill="none" stroke="#0e2742" stroke-width="1.1"/></svg>
          info@veldhaus.de
        </span>
        <span class="item">
          <svg viewBox="0 0 10 10"><path d="M5 0.5 A3.5 3.5 0 0 1 8.5 4 C8.5 6.3 5 9.5 5 9.5 C5 9.5 1.5 6.3 1.5 4 A3.5 3.5 0 0 1 5 0.5 Z" fill="#0e2742"/><circle cx="5" cy="4" r="1.3" fill="#bca663"/></svg>
          Lindenallee 12, 40210 Düsseldorf
        </span>
      </div>

      <h2 class="eyebrow">PROJEKTMANAGEMENT &amp; PROJEKTSTEUERUNG</h2>
      <h1 class="headline">WIR REALISIEREN<br>BAUVORHABEN</h1>

      <section class="cards">
        <article class="card">
          <p class="kicker">Betriebswirtschaftliche Planung</p>
          <h3 class="title">STET CLITA KASD GUBERGREN NO SEA<br>TAKIMATA SANCTUS EST LOREM IPSUM</h3>
          <p class="body">Lorem ipsum dolor sit amet, consetetur sadipscing elitr, sed diam nonumy eirmod tempor invidunt ut labore et dolore magna aliquyam erat, sed diam voluptua.</p>
          <span class="more">WEITERLESEN</span>
        </article>
        <article class="card">
          <p class="kicker">Steuerung der baulichen Umsetzung</p>
          <h3 class="title">STET CLITA KASD GUBERGREN NO SEA<br>TAKIMATA SANCTUS EST LOREM IPSUM</h3>
          <p class="body">Lorem ipsum dolor sit amet, consetetur sadipscing elitr, sed diam nonumy eirmod tempor invidunt ut labore et dolore magna aliquyam erat, sed diam voluptua.</p>
          <span class="more">WEITERLESEN</span>
        </article>
        <article class="card">
          <p class="kicker">Marketing und Vertrieb</p>
          <h3 class="title">STET CLITA KASD GUBERGREN NO SEA<br>TAKIMATA SANCTUS EST LOREM IPSUM</h3>
          <p class="body">Lorem ipsum dolor sit amet, consetetur sadipscing elitr, sed diam nonumy eirmod tempor invidunt ut labore et dolore magna aliquyam erat, sed diam voluptua.</p>
          <span class="more">WEITERLESEN</span>
        </article>
      </section>

      <footer class="footer">© 2017 Veldhaus Real Estate GmbH - Impressum</footer>
    </main>
  </div>
</body>
</html>
```